Need designers to make a boring check list funky and fun

We are an executive rental company based in Sydney. We deal in fully furnished properties for both short and long term bookings. We have a check list for home owners to help them prepare their home for guests.
We are looking for an interesting design which makes the mundane tasks seem both fun and enjoyable.
Target Market(s)
single, couples and families where they are dual income households. Highly educated, high powered jobs with little to no time and are stressed needing a break, but also needing to pay the mortgage.
Industry/Entity Type
It Company
Colors
Designer to choose colors to be used in the design.
Requirements
Must have
- images of house rooms, clean.
- our logo on it
Nice to have
- icons for each section ie person swimming for a pool
Should not have
- just text no images

```html
<!DOCTYPE html>
<html lang="en">
<head>
<meta charset="utf-8">
<title>Check list for Holiday Owners – Page 4</title>
<link href="https://fonts.googleapis.com/css2?family=Didact+Gothic&family=Montserrat:wght@600;700;800&display=swap" rel="stylesheet">
<style>
  :root {
    --brand: #e5194b;
    --brand-soft: #f07a95;
    --ink: #2a2a2a;
    --paper: #ffffff;
  }
  * { box-sizing: border-box; margin: 0; padding: 0; }
  html, body { width: 848px; height: 1200px; overflow: hidden; background: var(--paper); }
  body { position: relative; font-family: "Didact Gothic", "Century Gothic", sans-serif; color: var(--ink); }

  .masthead { position: absolute; top: 40px; left: 40px; width: 768px; height: 52px; }
  .masthead__mark { position: absolute; left: 0; top: 0; width: 52px; height: 52px; background: var(--brand); }
  .masthead__bar { position: absolute; left: 59px; right: 0; top: 0; height: 52px; background: var(--brand); color: #fff; }
  .masthead__name { position: absolute; left: 19px; top: 17px; font-size: 15px; letter-spacing: 1.6px; text-transform: uppercase; color: #fde2e8; }
  .masthead__doc { position: absolute; right: 20px; top: 8px; text-align: center; font-family: "Montserrat", sans-serif; font-weight: 700; font-size: 13.5px; line-height: 19px; }
  .masthead__doc em { display: block; font-size: 11.5px; font-weight: 700; }

  .section-head { position: absolute; height: 40px; background: var(--brand); color: #fff; }
  .section-head__title { position: absolute; left: 13px; top: 6px; font-family: "Montserrat", sans-serif; font-weight: 800; font-size: 25px; letter-spacing: 0.4px; }
  .section-head__num { font-family: "Didact Gothic", sans-serif; font-weight: 400; font-size: 21px; color: #fde2e8; margin-right: 4px; }
  .section-head__icon { position: absolute; right: 8px; top: -2px; width: 66px; height: 44px; background: #fff; border-radius: 22px; display: flex; align-items: center; justify-content: center; }
  .section-head__icon svg { width: 34px; height: 34px; }

  .checklist { position: absolute; list-style: none; font-size: 18px; line-height: 22.4px; }
  .checklist li { position: relative; padding-left: 22px; margin-bottom: 8px; }
  .checklist li::before { content: ""; position: absolute; left: 1px; top: 5px; width: 10px; height: 10px; border: 1.5px solid var(--brand); box-shadow: 2px 2px 0 var(--brand-soft); background: #fff; }

  .photo { position: absolute; left: 440px; top: 424px; width: 368px; height: 214px;
    background: linear-gradient(180deg, #a9cbe0 0%, #6c9a4f 30%, #3f6b2e 55%, #b9a48a 68%, #5bc4de 78%, #2ea7cf 100%);
    clip-path: polygon(28px 0, 100% 0, 100% calc(100% - 28px), calc(100% - 28px) 100%, 0 100%, 0 28px); }

  .footer { position: absolute; left: 40px; top: 1129px; width: 768px; height: 30px; background: var(--brand); color: #fff; font-family: "Montserrat", sans-serif; font-weight: 700; font-size: 17px; }
  .footer__item { position: absolute; top: 5px; display: flex; align-items: center; gap: 6px; }
  .footer__item svg { width: 14px; height: 14px; }
  .footer__phone { left: 20px; }
  .footer__web { right: 20px; }
</style>
</head>
<body>

<header class="masthead">
  <div class="masthead__mark"></div>
  <div class="masthead__bar">
    <span class="masthead__name">Harbourline Properties</span>
    <div class="masthead__doc">Check list for Holiday Owners<em>Page 4/4</em></div>
  </div>
</header>

<!-- Outside -->
<div class="section-head" style="left:40px; top:134px; width:768px;">
  <h2 class="section-head__title"><span class="section-head__num">9/12</span>OUTSIDE</h2>
  <div class="section-head__icon">
    <svg viewBox="0 0 34 34"><path d="M6 30 C4 16 12 5 30 4 C30 20 22 30 6 30 Z" fill="none" stroke="var(--brand)" stroke-width="3"/><path d="M6 30 L24 10" stroke="var(--brand)" stroke-width="3"/></svg>
  </div>
</div>
<ul class="checklist" style="left:42px; top:188px; width:380px;">
  <li>Ensure all balconies, railings, fences and flooring are stable and safe.</li>
  <li>Check height of balcony railings are compliant</li>
  <li>Get Gardener to tidy garden, weed, remove any dead branches and mulch garden beds.</li>
  <li>Arrange gardener to maintain gardens regularly (every 2 weeks) whilst you are away</li>
  <li>Ensure automatic watering system is installed and functioning</li>
  <li>Clean BBQ, fit pitts and outdoor heaters and ensure gas bottle is full if needed and or extra wood is provided.</li>
  <li>Jet blast mouldy or mildew from all outdoor surfaces</li>
  <li>Remove cobwebs</li>
</ul>
<ul class="checklist" style="left:442px; top:188px; width:370px;">
  <li>Clean out gutters</li>
  <li>Remove any stray item including pet toys.</li>
  <li>Ensure outdoor lighting is operational</li>
  <li>Ensure all pathways and stairs are safe and all gates are functioning and secure</li>
  <li>Parking, provide parking dimensions</li>
  <li>Windows to be cleaned and sparkling</li>
</ul>
<div class="photo" role="img" aria-label="Backyard swimming pool with a thatched umbrella, palm trees and lush tropical garden"></div>

<!-- Safety -->
<div class="section-head" style="left:40px; top:682px; width:368px;">
  <h2 class="section-head__title"><span class="section-head__num">10/12</span>SAFETY</h2>
  <div class="section-head__icon">
    <svg viewBox="0 0 34 34"><path d="M3 17 A14 13 0 0 1 31 17 Z" fill="var(--brand)"/><path d="M17 17 V28 a3 3 0 0 1 -6 0" fill="none" stroke="var(--brand)" stroke-width="3"/></svg>
  </div>
</div>
<ul class="checklist" style="left:42px; top:736px; width:370px;">
  <li>Provide fire extinguisher, fire blanket and first aid kit</li>
  <li>Repair leaking taps, broken tiles, etc</li>
  <li>Patch and holes in walls</li>
  <li>Check smoke alarms functioning</li>
</ul>

<!-- Insurance -->
<div class="section-head" style="left:440px; top:682px; width:368px;">
  <h2 class="section-head__title"><span class="section-head__num">11/12</span>INSURANCE</h2>
  <div class="section-head__icon">
    <svg viewBox="0 0 34 34"><circle cx="23" cy="11" r="8" fill="var(--brand)"/><circle cx="24" cy="10" r="2.5" fill="#fff"/><path d="M18 15 L5 28 M8 25 L11 28 M11 22 L14 25" stroke="var(--brand)" stroke-width="4"/></svg>
  </div>
</div>
<ul class="checklist" style="left:442px; top:736px; width:370px;">
  <li>Get landlord and Tenants insurance</li>
  <li>Take photos of contents and of your home</li>
  <li>Lock away any valuables</li>
</ul>

<!-- Final bits -->
<div class="section-head" style="left:40px; top:906px; width:768px;">
  <h2 class="section-head__title"><span class="section-head__num">12/12</span>YOU’RE ALMOST THERE... FINAL BITS</h2>
  <div class="section-head__icon">
    <svg viewBox="0 0 34 34"><circle cx="17" cy="17" r="14" fill="none" stroke="var(--brand)" stroke-width="3.5"/><path d="M10 17 L15 22 L24 12" fill="none" stroke="var(--brand)" stroke-width="3.5"/></svg>
  </div>
</div>
<ul class="checklist" style="left:42px; top:960px; width:760px;">
  <li>Provide 4 sets of keys for Harbourline Properties</li>
  <li>Arrange rubbish to be placed out on street when required (Harbourline can arrange this at a fee)</li>
  <li>Let Harbourline know of any areas which could be affected by heavy rain</li>
  <li>Cleaners come in to set up the property prior to guests arrival</li>
</ul>

<footer class="footer">
  <div class="footer__item footer__phone">
    <svg viewBox="0 0 14 14"><rect x="0" y="0" width="14" height="14" rx="3" fill="#fff"/><path d="M4 3 L6 5 L5 6.5 Q6 8.5 7.5 9 L9 8 L11 10 L9.5 11.5 Q4 10 2.5 4.5 Z" fill="var(--brand)"/></svg>
    +61 400 555 019 (during business hours)
  </div>
  <div class="footer__item footer__web">
    <svg viewBox="0 0 14 14"><rect x="0" y="0" width="14" height="14" rx="2" fill="#fff"/><path d="M4 10 L10 4 M6 4 H10 V8" stroke="var(--brand)" stroke-width="2" fill="none"/></svg>
    www.harbourline.com.au
  </div>
</footer>

</body>
</html>
```